Boutique Financial Services/Advisor Business Needs Web Design

Looking for an informational and functional web design for my Financial Services/Financial Advisement business. It should have functionality for Company name, address, phone #, "About Us", Who we are, Our Mission, Services we offer, Biographies/Photos of/about "The Team", and possibly a link to "Contact Us". Would like to see something new & exciting blended with a traditional/professional look that will appeal to those approaching retirement, as well as those younger clients that are beginning to think about planning for the future. I already have a web domain through Brixwell, but would like this to be the design we use for that domain.
Financial Services/Financial Advisor
Coded - Design and coding required
1 page

```html
<!DOCTYPE html>
<html lang="en">
<head>
<meta charset="utf-8">
<title>Summitline Wealth Management</title>
<link href="https://fonts.googleapis.com/css2?family=Jost:wght@400;500;600&family=Poppins:wght@400;500;600;700&display=swap" rel="stylesheet">
<style>
:root{
  --ink:#262626;
  --ink-soft:#3d3d3d;
  --navy:#1d2a5c;
  --accent:#4d74e4;
  --accent-light:#6f95ee;
  --deep:#1a1fb8;
  --card-line:#c9d4ef;
  --field:#f3f3f3;
  --field-line:#d9d9d9;
  --band:#cfdcf3;
  --footer:#f5efee;
  --white:#ffffff;
}
*{margin:0;padding:0;box-sizing:border-box}
html,body{width:1200px;height:4043px;overflow:hidden;background:var(--white)}
body{position:relative;font-family:"Poppins",sans-serif;color:var(--ink)}
.abs{position:absolute}
.heading{font-family:"Jost",sans-serif;font-weight:500;color:var(--ink);font-size:38px;line-height:49px}
.heading .hl{color:var(--accent)}
.label{font-family:"Jost",sans-serif;font-weight:500;font-size:17px;color:var(--ink)}
.body-text{font-size:14px;line-height:22px;color:var(--ink-soft)}
.btn{position:absolute;display:flex;align-items:center;justify-content:center;color:var(--white);font-weight:600;font-size:14px;background:linear-gradient(90deg,var(--accent-light),var(--deep));border-radius:26px 0 26px 0}
.ph{position:absolute}

/* header */
.logo{left:67px;top:40px;width:220px;font-family:"Poppins",sans-serif;font-weight:500;color:var(--navy);font-size:17px;line-height:22px;text-align:center}
.nav a{position:absolute;top:60px;font-size:14px;font-weight:600;color:var(--ink);text-decoration:none}
.nav .home{left:358px;top:35px;width:66px;height:66px;border-radius:50%;background:linear-gradient(135deg,var(--accent-light),var(--deep));color:var(--white);display:flex;align-items:center;justify-content:center}

/* hero */
.hero{left:0;top:141px;width:1200px;height:512px;background:linear-gradient(120deg,#0c2b3e 0%,#123b4f 35%,#0d2346 65%,#141a5e 100%);overflow:hidden}
.hero-welcome{left:63px;top:257px;color:var(--white);font-size:17px;font-family:"Jost",sans-serif;font-weight:500}
.hero-title{left:63px;top:290px;font-family:"Jost",sans-serif;font-size:39px;font-weight:500;color:var(--white)}
.hero-title .hl{color:var(--accent-light)}
.hero-text{left:63px;top:353px;width:620px;color:var(--white);font-size:14px;line-height:22px}

/* cards */
.card{position:absolute;top:1431px;width:339px;height:400px;border:1.5px solid var(--card-line);border-radius:4px;background:var(--white)}
.card .ph{left:16px;top:16px;width:305px;height:246px;border-radius:6px}
.card h3{position:absolute;left:16px;top:283px;font-family:"Jost",sans-serif;font-weight:500;font-size:18px}
.card p{position:absolute;left:16px;top:312px;width:300px;font-size:12px;line-height:18px;color:var(--ink-soft)}
.card svg{position:absolute;right:16px;top:364px}

/* team */
.member{position:absolute;top:1930px;width:318px;height:408px;border:1.5px solid var(--card-line);background:var(--white)}
.member .ph{left:12px;top:9px;width:292px;height:314px}
.member .plate{position:absolute;left:0;right:0;bottom:6px;height:72px;background:linear-gradient(90deg,#6f95ee,#1a1fb8);color:var(--white);text-align:center}
.member .plate b{display:block;font-size:20px;font-weight:700;margin-top:12px}
.member .plate span{font-size:12px}

/* faq */
.faq{position:absolute;left:519px;width:618px;height:53px;background:var(--field);border:1px solid var(--field-line);border-radius:3px;font-size:14px;padding:17px 12px}
.faq .plus{position:absolute;right:14px;top:18px;width:12px;height:12px;border-radius:50%;background:#9a9a9a;color:var(--white);font-size:10px;line-height:12px;text-align:center}

/* form */
.field{position:absolute;background:var(--field);border:1px solid var(--field-line);border-radius:3px;font-size:12px;color:#777;display:flex;align-items:center;gap:10px;padding-left:22px}

/* footer */
.footer{left:0;top:3731px;width:1200px;height:312px;background:var(--footer)}
.f-head{position:absolute;top:3764px;color:var(--accent);font-size:15px;font-weight:500}
.f-list{position:absolute;top:3800px;font-size:14px;line-height:37px;color:var(--ink)}
.social{position:absolute;top:3929px;width:26px;height:26px;border-radius:50%;background:var(--ink)}
</style>
</head>
<body>

<!-- header -->
<div class="abs logo">Summitline Wealth<br>Management</div>
<nav class="nav">
  <a class="home" href="#">Home</a>
  <a href="#" style="left:457px">About Us</a>
  <a href="#" style="left:579px">Services</a>
  <a href="#" style="left:700px">Our Team</a>
  <a href="#" style="left:828px">Contact Us</a>
</nav>
<div class="btn" style="left:1017px;top:47px;width:130px;height:47px">Get Started</div>

<!-- hero -->
<section class="abs hero"></section>
<div class="abs hero-welcome">Welcome to Summitline Wealth Management</div>
<h1 class="abs hero-title"><span class="hl">Your Trusted</span> Financial Partner</h1>
<p class="abs hero-text">At Summitline Wealth Management, we understand that navigating the world of finance can be overwhelming. Whether you're looking to grow your wealth, plan for retirement, manage your investments, or protect your assets, our team of expert financial advisors is here to help you every step of the way.</p>
<div class="btn" style="left:63px;top:455px;width:128px;height:47px">Get Started</div>
<div class="abs" style="left:1013px;top:154px;width:88px;height:88px;border-radius:50%;background:radial-gradient(circle at 30% 30%,#5b7bf0,#1a22c8)"></div>
<div class="abs" style="left:702px;top:196px;width:378px;height:378px;border-radius:50%;background:linear-gradient(160deg,#3a4ff0,#1e27c9)"></div>
<div class="abs" style="left:686px;top:515px;width:34px;height:34px;border-radius:50%;background:#2c38d8"></div>
<div class="ph" role="img" aria-label="Smiling financial advisor in a navy suit, arms folded on a desk" style="left:730px;top:196px;width:370px;height:486px;border-radius:180px 180px 30px 30px;background:linear-gradient(180deg,#c9a88f 0%,#1d2f6a 45%,#16224f 100%)"></div>

<!-- about -->
<div class="ph" role="img" aria-label="Hand holding a phone showing a payment successful screen over a laptop" style="left:58px;top:723px;width:449px;height:312px;background:linear-gradient(135deg,#d9d9d9,#6f6f6f 60%,#2b2b2b)"></div>
<svg class="abs" style="left:67px;top:1098px" width="60" height="76" viewBox="0 0 60 76" aria-hidden="true"><rect x="6" y="10" width="46" height="42" rx="4" fill="#2d57c8" transform="rotate(-10 29 31)"/><rect x="11" y="16" width="36" height="30" rx="2" fill="#ffffff" transform="rotate(-10 29 31)"/><text x="16" y="40" font-family="Poppins,sans-serif" font-size="13" font-weight="700" fill="#1d2a5c" transform="rotate(-10 29 31)">24/7</text><rect x="22" y="58" width="16" height="10" fill="#555"/></svg>
<div class="abs" style="left:168px;top:1095px;font-size:18px;font-weight:600">Offers 24/7 Access.</div>
<p class="abs body-text" style="left:168px;top:1130px;width:300px">Enjoy round-the-clock access to your accounts, allowing to finances.</p>

<div class="abs label" style="left:544px;top:724px">About Us</div>
<h2 class="abs heading" style="left:544px;top:764px;width:620px"><span class="hl">Passionate About Your</span> Financial Well-being</h2>
<p class="abs body-text" style="left:544px;top:880px;width:580px">&nbsp;Summitline Wealth Management, we believe in empowering individuals and businesses with the knowledge and tools to manage and grow their finances effectively.</p>
<div class="ph" role="img" aria-label="Two business people shaking hands over a glowing city skyline" style="left:544px;top:966px;width:516px;height:145px;border-radius:10px;background:linear-gradient(180deg,#0d0d12 0%,#1c2030 55%,#2a6a74 100%)"></div>
<div class="btn" style="left:544px;top:1130px;width:127px;height:47px">View More</div>

<!-- benefits -->
<div class="abs label" style="left:61px;top:1269px">Benefits of Financial Services</div>
<h2 class="abs heading" style="left:61px;top:1302px;width:780px"><span class="hl">Protect, Grow, and Optimize</span> Your Wealth with Tailored Financial Solutions</h2>

<div class="card" style="left:61px">
  <div class="ph" role="img" aria-label="Stacks of coins with a rising growth chart" style="background:linear-gradient(160deg,#9aa7b6,#2f4a60 55%,#1d2d3a)"></div>
  <h3>Wealth Management</h3>
  <p>Lorem ipsum dolor sit amet consectetur. Sed viverra tortor curabitur donec .</p>
  <svg width="26" height="20" viewBox="0 0 26 20"><path d="M1 10H24M16 2L24 10L16 18" stroke="#2d55d8" stroke-width="2" fill="none"/></svg>
</div>
<div class="card" style="left:425px">
  <div class="ph" role="img" aria-label="Smiling advisor in a white blouse shaking a client's hand" style="background:linear-gradient(160deg,#d6d8d8,#9aa1a6 55%,#3a4350)"></div>
  <h3>Financial Planning</h3>
  <p>Lorem ipsum dolor sit amet consectetur. Sed viverra tortor curabitur donec .</p>
  <svg width="26" height="20" viewBox="0 0 26 20"><path d="M1 10H24M16 2L24 10L16 18" stroke="#2d55d8" stroke-width="2" fill="none"/></svg>
</div>
<div class="card" style="left:789px">
  <div class="ph" role="img" aria-label="Hand adjusting a low to high risk slider with finance icons" style="background:linear-gradient(160deg,#1a3a4a,#0e2230 60%,#0a1620)"></div>
  <h3>Risk Management</h3>
  <p>Lorem ipsum dolor sit amet consectetur. Sed viverra tortor curabitur donec .</p>
  <svg width="26" height="20" viewBox="0 0 26 20"><path d="M1 10H24M16 2L24 10L16 18" stroke="#2d55d8" stroke-width="2" fill="none"/></svg>
</div>
<div class="card" style="left:1153px">
  <div class="ph" role="img" aria-label="Risk management illustration" style="background:linear-gradient(160deg,#1a3a4a,#0a1620)"></div>
  <h3>Risk Management</h3>
  <p>Lorem ipsum dolor sit amet consectetur.</p>
</div>
<svg class="abs" style="left:541px;top:1861px" width="106" height="5" viewBox="0 0 106 5"><rect width="20" height="5" rx="2" fill="#2d55d8"/><rect x="22" width="20" height="5" rx="2" fill="#d0d0d0"/><rect x="44" width="20" height="5" rx="2" fill="#d0d0d0"/><rect x="66" width="18" height="5" rx="2" fill="#d0d0d0"/><rect x="86" width="20" height="5" rx="2" fill="#d0d0d0"/></svg>

<!-- team -->
<div class="abs label" style="left:61px;top:1931px">Our Team</div>
<h2 class="abs heading" style="left:61px;top:1964px;width:360px">Meet The Experts Behind <span class="hl">Your Financial Success</span></h2>
<p class="abs body-text" style="left:61px;top:2122px;width:350px;font-size:13.5px">we believe that a strong, knowledgeable team is the key to providing exceptional financial services. Our experts are committed to helping you navigate the complexities of your financial journey with personalized advice and strategies. Here's a closer look at the professionals who make up our team:</p>
<div class="btn" style="left:61px;top:2291px;width:129px;height:47px">View More</div>

<div class="member" style="left:442px">
  <div class="ph" role="img" aria-label="Portrait of a smiling team member in glasses and a light blue shirt" style="background:linear-gradient(180deg,#e4e6e8,#b9c4d2 60%,#7f9bc0)"></div>
  <div class="plate"><b>Nora Ellis</b><span>Finance Support</span></div>
</div>
<div class="member" style="left:778px">
  <div class="ph" role="img" aria-label="Portrait of a team member in a knit cap seated at a table" style="background:linear-gradient(180deg,#c9a26f,#5b4a3a 60%,#2c2a2b)"></div>
  <div class="plate"><b>Marcus Reyes</b><span>Manager</span></div>
</div>

<!-- faq -->
<div class="abs label" style="left:64px;top:2464px">Frequently Asked Questions</div>
<h2 class="abs heading" style="left:64px;top:2497px;width:400px">Quick <span class="hl">Answers To Common</span> Questions</h2>
<p class="abs body-text" style="left:64px;top:2606px;width:390px;font-size:13.5px">Discover clear, concise answers to frequently asked questions. Let us help you get the information you need quickly and easily.</p>
<div class="abs" style="left:64px;top:2707px;font-size:14px">If you have a different question!</div>
<div class="btn" style="left:64px;top:2738px;width:129px;height:47px">Contact</div>

<div class="faq" style="top:2408px;height:102px;padding-top:20px">Lorem ipsum dolor sit amet, consectetur ?<div style="margin-top:10px;line-height:22px">Lorem ipsum dolor sit amet, consectetur adipiscing elit, sed do eiusmod tempor incididunt ut</div><span class="plus" style="top:17px">×</span></div>
<div class="faq" style="top:2524px">Lorem ipsum dolor sit amet, consectetur ?<span class="plus">+</span></div>
<div class="faq" style="top:2589px">Lorem ipsum dolor sit amet, consectetur ?<span class="plus">+</span></div>
<div class="faq" style="top:2654px">Lorem ipsum dolor sit amet, consectetur ?<span class="plus">+</span></div>
<div class="faq" style="top:2719px">Lorem ipsum dolor sit amet, consectetur ?<span class="plus">+</span></div>
<div class="faq" style="top:2784px">Lorem ipsum dolor sit amet, consectetur ?<span class="plus">+</span></div>

<!-- testimonial -->
<div class="abs" style="left:16px;top:2907px;width:1168px;height:333px;background:var(--band);border-radius:0 160px 0 160px"></div>
<div class="abs label" style="left:157px;top:2950px">Testimonial</div>
<h2 class="abs heading" style="left:157px;top:2992px;width:220px;line-height:40px"><span class="hl">Love</span> From Clients</h2>
<p class="abs body-text" style="left:157px;top:3094px;width:200px;font-size:13.5px">Hear what our satisfied clients have to say about our services</p>
<div class="ph" role="img" aria-label="Round portrait of a client in a dark jacket" style="left:449px;top:2953px;width:111px;height:106px;border-radius:50%;background:linear-gradient(160deg,#b0a79d,#3b3a3f)"></div>
<div class="abs" style="left:591px;top:2983px;font-size:15px;font-weight:600">Dana Whitfield</div>
<div class="abs" style="left:591px;top:3011px;font-size:12.5px">Regional Manager</div>
<svg class="abs" style="left:918px;top:2963px" width="72" height="17" viewBox="0 0 72 17" aria-label="4 stars"><g fill="#2d55d8"><path id="st" d="M8 0l2.4 5.3 5.6.5-4.3 3.8 1.3 5.6L8 12.3 3 15.2l1.3-5.6L0 5.8l5.6-.5z"/><use href="#st" x="18"/><use href="#st" x="36"/><use href="#st" x="54"/></g></svg>
<div class="abs" style="left:1020px;top:2962px;font-size:14px">4.6</div>
<p class="abs body-text" style="left:449px;top:3072px;width:510px;font-size:14.5px">"I've been using Summitline for over a year now, and it has completely changed the way I manage my finances. It's so easy to use and has helped me save time and stay on top of my accounts. Highly recommend!"</p>
<svg class="abs" style="left:548px;top:3203px" width="106" height="5" viewBox="0 0 106 5"><rect width="20" height="5" rx="2" fill="#2d55d8"/><rect x="22" width="20" height="5" rx="2" fill="#9aa6c4"/><rect x="44" width="20" height="5" rx="2" fill="#9aa6c4"/><rect x="66" width="18" height="5" rx="2" fill="#9aa6c4"/><rect x="86" width="20" height="5" rx="2" fill="#9aa6c4"/></svg>

<!-- contact -->
<h2 class="abs heading" style="left:64px;top:3298px;width:330px;line-height:41px">Contact With <span class="hl">Our Team</span></h2>
<p class="abs" style="left:64px;top:3394px;width:380px;font-size:14px;line-height:22px">If You Have Question, Please Use Our 24-7 &nbsp;Hours Helpline</p>
<div class="ph" role="img" aria-label="Smiling support agents wearing headsets" style="left:64px;top:3452px;width:394px;height:211px;border-radius:6px;background:linear-gradient(120deg,#c7b09a,#7a6a5c 50%,#bfc7d6)"></div>

<div class="field" style="left:613px;top:3303px;width:521px;height:47px"><svg width="22" height="22" viewBox="0 0 22 22"><circle cx="11" cy="7" r="5" stroke="#888" stroke-width="1.4" fill="none"/><path d="M2 21c1-5 5-7 9-7s8 2 9 7" stroke="#888" stroke-width="1.4" fill="none"/></svg>Name*</div>
<div class="field" style="left:613px;top:3370px;width:251px;height:47px"><svg width="26" height="18" viewBox="0 0 26 18"><rect x="1" y="1" width="24" height="16" rx="2" stroke="#888" stroke-width="1.4" fill="none"/><path d="M1 2l12 9 12-9" stroke="#888" stroke-width="1.4" fill="none"/></svg>Email*</div>
<div class="field" style="left:883px;top:3370px;width:251px;height:47px"><svg width="22" height="22" viewBox="0 0 22 22"><path d="M4 2l4 1 1 5-2 2c1 3 3 5 6 6l2-2 5 1 1 4-3 2C9 20 2 13 1 5z" stroke="#888" stroke-width="1.4" fill="none"/></svg>Number*</div>
<div class="field" style="left:613px;top:3436px;width:521px;height:50px"><svg width="22" height="22" viewBox="0 0 22 22"><path d="M2 2h9l9 9-9 9-9-9z" stroke="#888" stroke-width="1.4" fill="none"/><circle cx="7" cy="7" r="1.5" fill="#888"/></svg>Subject*</div>
<div class="field" style="left:613px;top:3507px;width:521px;height:102px;align-items:flex-start;padding-top:16px">Message*</div>
<div class="btn" style="left:613px;top:3627px;width:129px;height:41px">Submit</div>

<!-- footer -->
<footer class="abs footer"></footer>
<div class="f-head" style="left:61px">Quick Contact</div>
<div class="abs" style="left:61px;top:3802px;font-size:14px;line-height:22px">1420 Maple Crest Avenue, Suite 210<br>Dayton, OH</div>
<div class="abs" style="left:61px;top:3860px;font-size:14px">hello@summitlinewealth.com</div>
<div class="abs" style="left:61px;top:3897px;font-size:14px">555-214-7730</div>

<div class="f-head" style="left:328px">Information</div>
<div class="f-list" style="left:328px">Home<br>About Us<br>Services<br>Our Team<br>Contact Us</div>

<div class="f-head" style="left:532px">Resources</div>
<div class="f-list" style="left:532px">Terms Of Condition<br>Privacy Policy<br>Cookies</div>

<div class="f-head" style="left:725px">Subscribe Newsletter</div>
<p class="abs" style="left:725px;top:3800px;width:420px;font-size:14px;line-height:22px">Join Now To Receive Exclusive Updates, Insights, And Resources Right In Your Inbox.</p>
<div class="abs" style="left:725px;top:3860px;width:251px;height:50px;background:var(--white);font-size:12px;color:#555;padding:17px 14px">Enter Your Email</div>
<div class="abs" style="left:976px;top:3860px;width:164px;height:50px;background:linear-gradient(90deg,#3a5ef0,#1a1fb8);color:var(--white);font-weight:600;font-size:15px;display:flex;align-items:center;justify-content:center">Subscribe</div>
<div class="social" style="left:725px"></div>
<div class="social" style="left:763px"></div>
<div class="social" style="left:801px"></div>
<div class="social" style="left:839px"></div>

<div class="abs" style="left:64px;top:3990px;width:1074px;height:1px;background:#b9b9b9"></div>
<div class="abs" style="left:0;top:4010px;width:1200px;text-align:center;font-size:12px">2024 Copyright ©<b>Summitline Wealth Management</b> Inc All Rights Reserved</div>

</body>
</html>
```